WP website design for Belcourt

We need a wordpress design for an established auction and real estate company based in New Jersey. The winning design will incorporate a professional color scheme with company logo in a clean layout. The design needs to consider that this will be developed on a responsive theme. Colors are those that will highlight the logo

Industry/Entity Type

Real Estate

Font styles to use
Serif
Sans Serif

Requirements
Must have
• colors will be #3E3D5D and #3C7296
navigation: 1) Home 2) Auctions 3) Real Estate Listings 4) Buyers 5) Sellers 6) About Us 7 ) Contact Us
design will use a slideshow - image is attached.
Widgets to place in the header, sidebar or footer:
1) email signup form 2) social icons (facebook, twitter, youtube, RSS) 3) Featured Properties widget 4) Featured Auctions widget 5) News & Events blog 6) Featured Videos
Nice to have
• Site will have numerous dropdown menus - so it would be nice to have a sample of what the dropdowns would look like. EG 1)▪ Our Featured Listings and 2)▪ MLS Property Search under the main "Real Estate Listings" menu item.

```html
<!DOCTYPE html>
<html lang="en">
<head>
<meta charset="utf-8">
<title>Belcourt Real Estate &amp; Auction</title>
<link href="https://fonts.googleapis.com/css2?family=Open+Sans:wght@400;600;700&family=Raleway:wght@500;600&family=Roboto+Slab:wght@700&family=Arimo:wght@400;700&family=Bitter:wght@400;700&display=swap" rel="stylesheet">
<style>
:root{
  --navy:#3E3D5D;
  --navy-line:#34334f;
  --blue:#3C7296;
  --blue-dark:#2f5d7d;
  --page:#d8d8d8;
  --white:#ffffff;
  --ink:#1e1e1e;
  --text:#333;
  --panel:#ededed;
  --line:#c4c4c4;
  --red:#e0171b;
  --teal:#2f8a9a;
  --footer:#2b2b2b;
}
*{box-sizing:border-box;margin:0;padding:0}
html,body{width:720px;height:1200px;overflow:hidden}
body{position:relative;background:var(--page);font-family:"Arimo",Arial,sans-serif;color:var(--ink)}
.abs{position:absolute}
.nav-band{left:0;top:97px;width:720px;height:159px;background:var(--navy)}
.column{left:61px;top:254px;width:597px;height:836px;background:var(--white)}
.header{left:61px;top:0;width:597px;height:97px;background:var(--white)}
.brand{left:25px;top:22px;display:flex;align-items:flex-start;gap:8px}
.brand-mark{width:22px;height:22px;background:var(--navy);margin-top:4px}
.brand-name{font-family:"Open Sans",sans-serif;font-weight:700;color:var(--navy);font-size:24px;line-height:26px}
.brand-name small{display:block;font-size:8.5px;line-height:11px;letter-spacing:.3px}
.social{left:443px;top:21px;display:flex;gap:6px}
.social span{width:26px;height:26px;border-radius:50%}
.contact-line{left:376px;top:66px;font-size:8.5px;display:flex;gap:12px;align-items:center}
.contact-line span{display:flex;align-items:center;gap:4px}
.nav{left:61px;top:97px;width:597px;height:29px;display:flex;background:var(--navy);z-index:2}
.nav a{display:flex;align-items:center;justify-content:center;color:var(--white);font-family:"Open Sans",sans-serif;font-size:9.5px;text-decoration:none;border-right:1px solid var(--navy-line);height:29px;white-space:nowrap}
.nav a.active{background:var(--blue)}
.nav-line{left:61px;top:126px;width:597px;height:2px;background:var(--white)}
.dropdown{left:198px;top:128px;width:128px;background:var(--blue);z-index:2}
.dropdown a{display:block;height:25px;line-height:25px;padding-left:11px;color:var(--white);font-family:"Open Sans",sans-serif;font-weight:700;font-size:8.5px;text-decoration:none}
.dropdown a + a{background:var(--blue-dark)}
.slide{left:61px;top:128px;width:415px;height:224px;background:linear-gradient(160deg,#9fb7c9 0%,#c9c4b1 35%,#6f8a4e 62%,#3e5a2a 100%)}
.dots{left:231px;top:336px;display:flex;gap:6px}
.dots i{width:7px;height:7px;border-radius:50%;background:#fff;border:1px solid #333}
.dots i.on{background:#333;border-color:#fff}
.share{left:437px;top:145px}
.signup{left:476px;top:128px;width:182px;height:224px;background:var(--blue);color:var(--white);overflow:hidden}
.signup p{position:absolute;left:18px;top:18px;width:150px;font-size:8.3px;line-height:12px}
.signup .field{position:absolute;left:21px;width:132px;height:20px;background:var(--white);border-radius:3px;color:#666;font-size:8px;line-height:20px;padding-left:10px;font-family:"Open Sans",sans-serif}
.signup .btn{position:absolute;left:22px;top:144px;width:73px;height:22px;background:var(--navy);border-radius:3px;text-align:center;line-height:22px;font-family:"Open Sans",sans-serif;font-size:12px}
.signup .at{position:absolute;left:110px;top:140px;font-size:72px;line-height:1;color:rgba(255,255,255,.28);font-family:"Arimo",sans-serif;font-weight:700}
.intro{left:74px;top:370px;width:384px;font-size:8.4px;line-height:10.8px;color:#222}
.card{left:72px;width:376px;height:200px;background:#f3f3f3;border:1px solid var(--line)}
.card-head{height:27px;background:var(--navy);color:var(--white);font-family:"Open Sans",sans-serif;font-weight:700;font-size:11px;line-height:29px;padding-left:13px;border-radius:6px 6px 0 0}
.card-photo{position:absolute;left:21px;top:35px;width:96px;height:64px;background:linear-gradient(180deg,#c6d2dc 0%,#c6d2dc 20%,#7c8f57 24%,#5c7338 100%);box-shadow:2px 2px 3px rgba(0,0,0,.35)}
.card-date{position:absolute;left:134px;top:38px;font-family:"Roboto Slab",serif;font-weight:700;color:var(--red);font-size:12.5px;line-height:14.5px}
.card-sell{position:absolute;left:135px;top:69px;font-family:"Bitter",serif;font-size:7px;line-height:10.5px;letter-spacing:.3px;width:225px;color:var(--text)}
.card-link{position:absolute;left:190px;top:96px;font-family:"Bitter",serif;font-weight:700;font-size:8.5px;color:var(--blue)}
.card-btn{position:absolute;left:43px;width:62px;height:19px;background:var(--blue);border-radius:3px;color:var(--white);font-size:8px;display:flex;align-items:center;gap:6px;padding-left:7px;font-family:"Open Sans",sans-serif}
.card-meta{position:absolute;left:135px;top:115px;font-family:"Bitter",serif;font-size:7.8px;line-height:11.6px}
.card-meta b{letter-spacing:.3px}
.card-meta .pin{display:inline-block;width:6px;height:8px;margin-right:3px;vertical-align:-1px}
.video{left:476px;top:378px;width:171px;height:150px;background:linear-gradient(180deg,#b9c7d3 0%,#dfe4e8 40%,#5e8a3a 60%,#3f6a25 100%)}
.video-bar{position:absolute;left:0;bottom:0;width:171px;height:12px;background:#111;color:#ddd;font-size:5.5px;display:flex;align-items:center;gap:4px;padding:0 4px}
.video-bar .track{flex:1;height:2px;background:#555}
.play{position:absolute;left:60px;top:53px;width:50px;height:30px;background:rgba(40,40,40,.75);border-radius:4px}
.widget{left:476px;width:171px;background:var(--panel);border:1px solid var(--line)}
.widget h3{font-family:"Raleway",sans-serif;font-weight:500;font-size:15.5px;color:#333;margin:6px 0 0 12px}
.widget .kicker{font-family:"Open Sans",sans-serif;font-weight:700;color:var(--teal);font-size:7.7px;text-align:center;margin-top:5px}
.widget .pic{width:128px;height:65px;margin:8px auto 0;border:2px solid #444}
.widget .cap{font-size:7.6px;line-height:10px;text-align:center;margin-top:9px}
.news-item{position:absolute;left:5px;width:155px}
.news-thumb{position:absolute;left:0;top:0;width:40px;height:28px;background:linear-gradient(180deg,#c9d2da 0%,#8a3d35 45%,#6d2c27 80%,#cfcfcf 100%);border:1px solid #999}
.news-text{position:absolute;left:49px;top:0;font-size:7.8px;line-height:10.8px;width:110px}
.news-more{position:absolute;left:99px;font-size:7.6px}
.footer{left:0;top:1090px;width:720px;height:86px;background:var(--footer)}
.footer h4{position:absolute;left:59px;top:12px;font-family:"Raleway",sans-serif;font-weight:600;color:#e8e8e8;font-size:11.5px}
.footer p{position:absolute;left:59px;font-size:8px;color:#a8a8a8}
.badge{position:absolute;background:#d9d9d9}
.footer-brand{position:absolute;left:584px;top:26px;font-family:"Open Sans",sans-serif;font-weight:700;color:#cfcfcf;font-size:15px;line-height:16px;text-align:center}
.footer-brand small{display:block;font-size:6px;line-height:8px}
.bottom{left:0;top:1176px;width:720px;height:24px;background:var(--navy);color:var(--white);font-size:8.3px;text-align:center;line-height:24px}
.bottom u{text-decoration:underline}
</style>
</head>
<body>
<div class="abs nav-band"></div>
<div class="abs column"></div>

<header class="abs header">
  <div class="abs brand">
    <div class="brand-mark"></div>
    <div class="brand-name">BELCOURT<small>REAL ESTATE &amp; AUCTION</small></div>
  </div>
  <div class="abs social" aria-label="Social links">
    <span style="background:#0f4a78"></span>
    <span style="background:#1da0e0"></span>
    <span style="background:#c8151a"></span>
    <span style="background:#f39a12"></span>
  </div>
  <div class="abs contact-line">
    <span><svg width="10" height="10" viewBox="0 0 10 10"><path d="M2 1 L4 3 L3 4.5 Q4.5 6.5 5.5 7 L7 6 L9 8 L7.5 9.5 Q2 8 0.5 2.5 Z" fill="#3C7296"/></svg>(555) 410 2286</span>
    <span><svg width="12" height="9" viewBox="0 0 12 9"><rect x="0.5" y="0.5" width="11" height="8" fill="#3C7296"/><path d="M0.5 0.5 L6 5 L11.5 0.5" stroke="#fff" fill="none"/></svg>info@belcourtauction.com</span>
  </div>
</header>

<nav class="abs nav">
  <a style="width:57px">HOME</a>
  <a style="width:81px">AUCTIONS</a>
  <a class="active" style="width:127px">REAL ESTATE LISTINGS</a>
  <a style="width:78px">BUYERS</a>
  <a style="width:73px">SELLERS</a>
  <a style="width:81px">ABOUT US</a>
  <a style="width:100px;border-right:0">CONTACT US</a>
</nav>
<div class="abs nav-line"></div>

<div class="abs slide" role="img" aria-label="Slideshow photo of a suburban house with a garden in front"></div>
<div class="abs dots"><i></i><i></i><i class="on"></i><i></i><i></i><i></i></div>
<svg class="abs share" width="16" height="16" viewBox="0 0 16 16"><circle cx="8" cy="8" r="8" fill="#111"/><path d="M4 11 Q5 6 9 6 V4 L12.5 7.5 L9 11 V8.5 Q6 8.5 4 11Z" fill="#fff"/></svg>

<div class="abs dropdown">
  <a>Our Featured Listings</a>
  <a>MLS Property Search</a>
</div>

<aside class="abs signup">
  <p>To start receiving email notifications for upcoming auctions, just fill in the fields below and click Subscribe.</p>
  <div class="field" style="top:74px">Name</div>
  <div class="field" style="top:107px">Email Address</div>
  <div class="btn">Subscribe</div>
  <div class="at">@</div>
</aside>

<p class="abs intro">For over 30 years, we have been a full service Real Estate &amp; Auction Company whose greatest desire is to meet and exceed your business and personal needs. Whether it is a multi-million $$$ farm, commercial real estate, an Estate, personal property, equipment or consultations, our goal is 100% client and customer satisfaction.</p>

<section class="abs card" style="top:432px">
  <div class="card-head">LAND AUCTION</div>
  <div class="card-photo" role="img" aria-label="Photo of open grassland"></div>
  <div class="card-date">THURSDAY, AUGUST 21ST AT<br>10:00 A.M.</div>
  <div class="card-sell">SELLING 3120 ACRES OF LAND IN TRACTS OF 2590 ACRES &amp; 560 ACRES</div>
  <div class="card-link">Click here to view Sale Bill!</div>
  <div class="card-btn" style="top:114px"><svg width="11" height="10"><rect x="1" y="1" width="8" height="8" fill="#fff"/></svg>Details</div>
  <div class="card-btn" style="top:141px"><svg width="11" height="10"><rect x="1" y="1" width="9" height="8" fill="#f2c230"/></svg>Photos</div>
  <div class="card-meta"><b>LIVE OFF-SITE AUCTION</b><br><b>Auction Location:</b><br><svg class="pin" viewBox="0 0 6 8"><path d="M3 8 L0.3 3.5 A3 3 0 1 1 5.7 3.5Z" fill="#d11"/></svg>48 Orchard Lane, Halden, OK 73900<br><b>Property Location:</b><br><svg class="pin" viewBox="0 0 6 8"><path d="M3 8 L0.3 3.5 A3 3 0 1 1 5.7 3.5Z" fill="#d11"/></svg>48 Orchard Lane, Halden, OK 73900<br><b>Begins:</b>&nbsp; 08/21/14 at 10:00 AM CDT</div>
</section>

<section class="abs card" style="top:652px">
  <div class="card-head">LAND AUCTION</div>
  <div class="card-photo" role="img" aria-label="Photo of open grassland"></div>
  <div class="card-date">THURSDAY, AUGUST 21ST AT<br>10:00 A.M.</div>
  <div class="card-sell">SELLING 3120 ACRES OF LAND IN TRACTS OF 2590 ACRES &amp; 560 ACRES</div>
  <div class="card-link">Click here to view Sale Bill!</div>
  <div class="card-btn" style="top:114px"><svg width="11" height="10"><rect x="1" y="1" width="8" height="8" fill="#fff"/></svg>Details</div>
  <div class="card-btn" style="top:141px"><svg width="11" height="10"><rect x="1" y="1" width="9" height="8" fill="#f2c230"/></svg>Photos</div>
  <div class="card-meta"><b>LIVE OFF-SITE AUCTION</b><br><b>Auction Location:</b><br><svg class="pin" viewBox="0 0 6 8"><path d="M3 8 L0.3 3.5 A3 3 0 1 1 5.7 3.5Z" fill="#d11"/></svg>48 Orchard Lane, Halden, OK 73900<br><b>Property Location:</b><br><svg class="pin" viewBox="0 0 6 8"><path d="M3 8 L0.3 3.5 A3 3 0 1 1 5.7 3.5Z" fill="#d11"/></svg>48 Orchard Lane, Halden, OK 73900<br><b>Begins:</b>&nbsp; 08/21/14 at 10:00 AM CDT</div>
</section>

<section class="abs card" style="top:874px">
  <div class="card-head">LAND AUCTION</div>
  <div class="card-photo" role="img" aria-label="Photo of open grassland"></div>
  <div class="card-date">THURSDAY, AUGUST 21ST AT<br>10:00 A.M.</div>
  <div class="card-sell">SELLING 3120 ACRES OF LAND IN TRACTS OF 2590 ACRES &amp; 560 ACRES</div>
  <div class="card-link">Click here to view Sale Bill!</div>
  <div class="card-btn" style="top:114px"><svg width="11" height="10"><rect x="1" y="1" width="8" height="8" fill="#fff"/></svg>Details</div>
  <div class="card-btn" style="top:141px"><svg width="11" height="10"><rect x="1" y="1" width="9" height="8" fill="#f2c230"/></svg>Photos</div>
  <div class="card-meta"><b>LIVE OFF-SITE AUCTION</b><br><b>Auction Location:</b><br><svg class="pin" viewBox="0 0 6 8"><path d="M3 8 L0.3 3.5 A3 3 0 1 1 5.7 3.5Z" fill="#d11"/></svg>48 Orchard Lane, Halden, OK 73900<br><b>Property Location:</b><br><svg class="pin" viewBox="0 0 6 8"><path d="M3 8 L0.3 3.5 A3 3 0 1 1 5.7 3.5Z" fill="#d11"/></svg>48 Orchard Lane, Halden, OK 73900<br><b>Begins:</b>&nbsp; 08/21/14 at 10:00 AM CDT</div>
</section>

<div class="abs video" role="img" aria-label="Featured video still of a farm field under a cloudy sky">
  <div class="play"><svg width="50" height="30"><path d="M20 7 L33 15 L20 23Z" fill="#fff"/></svg></div>
  <div class="video-bar"><span>&#9654;</span><span>00:00</span><span class="track"></span><span>00:00</span></div>
</div>

<section class="abs widget" style="top:545px;height:165px">
  <h3>Featured Auctions</h3>
  <div class="kicker">13.35 ACRES OF PRIME DEVELOP</div>
  <div class="pic" role="img" aria-label="Photo of a crowd gathered outside a large white house" style="background:linear-gradient(180deg,#cfd9e2 0%,#a8b5bf 40%,#5d7a45 70%,#3f5a2e 100%)"></div>
  <div class="cap">LOTS 13 &amp; 14 FOR SALE, FENWICK<br>IOWA<br>Mill Street, Fenwick, IA 52700</div>
</section>

<section class="abs widget" style="top:726px;height:165px">
  <h3>Featured Properties</h3>
  <div class="kicker">13.35 ACRES OF PRIME DEVELOP</div>
  <div class="pic" role="img" aria-label="Photo of a large brick house" style="background:linear-gradient(180deg,#5b86c4 0%,#8fb0dc 30%,#9a4d3a 45%,#7a3a2c 80%,#5f7d3c 100%)"></div>
  <div class="cap">LOTS 13 &amp; 14 FOR SALE, FENWICK<br>IOWA<br>Mill Street, Fenwick, IA 52700</div>
</section>

<section class="abs widget" style="top:907px;height:167px">
  <h3 style="margin-top:8px">News &amp; Events</h3>
  <div class="news-item" style="top:46px">
    <div class="news-thumb" role="img" aria-label="Thumbnail photo of a brick house"></div>
    <div class="news-text">Hartline HX3 High Lift, 600 Series Torvik tractor</div>
    <div class="news-more" style="top:36px">Read More...</div>
  </div>
  <div style="position:absolute;left:8px;top:94px;width:155px;height:1px;background:#d2d2d2"></div>
  <div class="news-item" style="top:112px">
    <div class="news-thumb" role="img" aria-label="Thumbnail photo of a brick house"></div>
    <div class="news-text" style="left:53px">Hartline HX3 High Lift, 600 Series Torvik tractor</div>
    <div class="news-more" style="top:34px">Read More...</div>
  </div>
</section>

<footer class="abs footer">
  <h4>Belcourt Real Estate &amp; Auction</h4>
  <p style="top:33px">Phone: (555) 304-2271</p>
  <p style="top:46px">Email: belcourtrealestate@mail.com</p>
  <p style="top:60px">Address: 1180 Linden Row, Millbrook, NJ 07801</p>
  <div class="badge" style="left:331px;top:20px;width:28px;height:30px"></div>
  <div class="badge" style="left:371px;top:26px;width:81px;height:22px"></div>
  <div class="badge" style="left:463px;top:26px;width:71px;height:24px;background:#9a9a9a"></div>
  <div class="badge" style="left:545px;top:26px;width:28px;height:28px;border-radius:50%;background:#bdbdbd"></div>
  <div class="footer-brand">BELCOURT<small>REAL ESTATE &amp; AUCTION</small></div>
</footer>
<div class="abs bottom">Copyright &copy; 2014 Ellison <u>Belcourt Real Estate &amp; Auction</u> All Rights Reserved.</div>
</body>
</html>
```